Brivo Wellness Co Business Card for food and Beverage Wizards & Alchemists

One main business card design for a wellness enterprise which represents two brands. We need one primary card design, for two different employees. The only difference between the cards will be the name, title and phone number for each employee, all other design elements will be same.
I've uploaded the logos for each brand. I have also uploaded a mockup which I made using Google's drawing tool. I can provide example images of business cards we find attractive if you would like some help picturing what we like.
I'm picturing the color splash on the back of the card below the two logos to be a dark burgundy or blue. This may sound a bit silly but the feel of the card and color should look almost like wizard dress robes. Dark emerald green, dark blue and dark burgundy with black undertones and gold lace.

Target Market(s)

Healthy food and beverage industry

Industry/Entity Type

Health And Wellness

Contact Information for Business Card

On one side we would like the business name, location, title of employee, employee name and contact details. On the flip side we would like our two brand logos and a splash of color. We would like the card to have a black font with some gold accents if possible. We would also like the trim of the business card or a middle ply within the card stock to have a color other than white.

Font styles to use
Serif

Colors
ec1f27
0255a3
00a990

Requirements
Must have
• Bold dark colors, happy to provide sample photos of business cards I like from pinterest. Must have a version for two different employees. Must be sharp, modern and chic.
Nice to have
• Thick card stock layer in between the front and back of card that is either black or gold lace or something to make it feel, well let's say to make it feel expensive.
Should not have
• Should not have any cartoon-ey elements. All business.

```html
<!DOCTYPE html>
<html lang="en">
<head>
<meta charset="utf-8">
<title>Brivo Wellness Co – Business Card</title>
<link rel="stylesheet" href="https://fonts.googleapis.com/css2?family=Source+Sans+3:wght@400;600&display=swap">
<style>
  :root {
    --backdrop: #555555;
    --card-black: #000000;
    --card-white: #ffffff;
    --ink: #111111;
    --text-light: #f2f2f2;
    --gold: #e8ac00;
    --burgundy: #5e0a1c;
  }
  * { margin: 0; padding: 0; box-sizing: border-box; }
  html, body {
    width: 1200px; height: 900px; overflow: hidden;
    background: var(--backdrop);
    font-family: "Source Sans 3", "Myriad Pro", sans-serif;
  }
  .stage { position: relative; width: 1200px; height: 900px; }
  .card {
    position: absolute; top: 170px;
    width: 347px; height: 561px; overflow: hidden;
  }
  .card-front { left: 259px; background: var(--card-black); color: var(--text-light); text-align: center; }
  .card-back { left: 631px; background: var(--card-white); }

  .company { position: absolute; top: 70px; width: 100%; }
  .company-name { font-size: 23px; font-weight: 600; letter-spacing: -0.2px; line-height: 1.1; }
  .company-location { font-size: 21.5px; font-weight: 400; line-height: 1.2; margin-top: 1px; }

  .person { position: absolute; top: 333px; width: 100%; }
  .person-name { font-size: 27px; font-weight: 600; color: var(--gold); line-height: 1.1; }
  .person-title { font-size: 21px; font-weight: 400; line-height: 1.35; }

  .contact-icons { position: absolute; top: 422px; left: 0; width: 100%; display: flex; justify-content: center; gap: 8px; }
  .contact-icon { width: 25px; height: 25px; }
  .contact-details { position: absolute; top: 457px; width: 100%; line-height: 25px; }
  .contact-phone { font-size: 21px; }
  .contact-email { font-size: 20px; }

  .brand-mark {
    position: absolute; left: 0; width: 100%; text-align: center;
    font-size: 22px; font-weight: 600; color: var(--ink);
  }
  .brand-primary { top: 62px; }
  .brand-secondary { top: 220px; }
  .robe-splash { position: absolute; inset: 0; }
</style>
</head>
<body>
<main class="stage">
  <section class="card card-front">
    <div class="company">
      <h1 class="company-name">Brivo Wellness Co</h1>
      <p class="company-location">Oakvale,CA</p>
    </div>
    <div class="person">
      <h2 class="person-name">Marcus Ellery</h2>
      <p class="person-title">Beverage Alchemist</p>
    </div>
    <div class="contact-icons">
      <svg class="contact-icon" viewBox="0 0 24 24" aria-label="Phone">
        <circle cx="12" cy="12" r="12" fill="var(--gold)"/>
        <path d="M8.2 6.5c.5-.4 1.1-.3 1.4.2l1.1 1.8c.3.5.2 1-.2 1.4l-.7.6c.6 1.4 1.6 2.4 3 3l.6-.7c.4-.4.9-.5 1.4-.2l1.8 1.1c.5.3.6.9.2 1.4l-.8 1c-.5.6-1.4.8-2.2.5-3.2-1.2-5.5-3.5-6.7-6.7-.3-.8-.1-1.700.5-2.2z" fill="#000"/>
      </svg>
      <svg class="contact-icon" viewBox="0 0 24 24" aria-label="Email">
        <circle cx="12" cy="12" r="12" fill="var(--gold)"/>
        <rect x="6.5" y="8" width="11" height="8" fill="#000"/>
        <path d="M6.5 8.3l5.5 4.2 5.5-4.2" fill="none" stroke="var(--gold)" stroke-width="1.1"/>
      </svg>
    </div>
    <div class="contact-details">
      <p class="contact-phone">415.555.0142</p>
      <p class="contact-email">brivowellnessco@mail.com</p>
    </div>
  </section>

  <section class="card card-back">
    <p class="brand-mark brand-primary">Brivo Wellness Co</p>
    <p class="brand-mark brand-secondary">Arcana Tonics</p>
    <svg class="robe-splash" viewBox="0 0 347 561" aria-hidden="true">
      <polygon points="0,457 347,250 347,561 0,561" fill="var(--burgundy)"/>
      <line x1="0" y1="470" x2="347" y2="263" stroke="var(--gold)" stroke-width="1.5"/>
    </svg>
  </section>
</main>
</body>
</html>
```